3" Round Business Card for Funeral Home

We need a business card designed for our cremation service. We would like to use a 3" round business card.

The business card will be 2-sided. One side with the logo featured prominently. The back sad will have employee name and contact info.

Templates for printing have been attached to project as well as logo

We like soft colors like the logo. Final design should promote a feeling of trust.

Industry/Entity Type

Funeral

Contact Information for Business Card

Employee Name, Phone number, email, web address

Requirements
Should not have
• any sort of funeral item such as urn, casket, hearse, tombstone

```html
<!DOCTYPE html>
<html lang="en">
<head>
<meta charset="utf-8">
<title>Stillwater Care – Round Business Card</title>
<link rel="stylesheet" href="https://fonts.googleapis.com/css2?family=Open+Sans:wght@400;700&display=swap">
<style>
  :root {
    --backdrop: #adadad;
    --card-light: #ffffff;
    --card-dark: #242424;
    --teal: #1a9e96;
    --plum: #8b1a8b;
    --ink: #1e1e1e;
    --dove-tone: #e9e9ec;
    --dove-shade: #c9c9ce;
  }
  * { margin: 0; padding: 0; box-sizing: border-box; }
  html, body {
    width: 1200px; height: 900px; overflow: hidden;
    background: var(--backdrop);
    font-family: "Open Sans", Arial, sans-serif;
  }
  .canvas { position: relative; width: 1200px; height: 900px; }

  .card {
    position: absolute;
    width: 414px; height: 414px;
    border-radius: 50%;
    top: 215px;
  }
  .card--front { left: 165px; background: var(--card-light); overflow: hidden; }
  .card--back  { left: 623px; background: var(--card-dark); }

  .brand-name {
    position: absolute;
    font-weight: 400;
    color: var(--teal);
    white-space: nowrap;
    letter-spacing: -0.5px;
  }
  .card--front .brand-name { left: 67px; top: 96px; font-size: 36px; }
  .card--back .brand-name { left: 0; right: 0; text-align: center; top: 178px; font-size: 38px; }

  .person { position: absolute; left: 67px; top: 178px; }
  .person__name { font-size: 24px; font-weight: 700; color: var(--teal); line-height: 1.2; }
  .person__title { font-size: 16.5px; color: var(--plum); line-height: 1.3; }
  .person__rule { width: 143px; height: 2px; background: var(--plum); margin-top: 8px; }

  .contacts { position: absolute; left: 67px; top: 259px; list-style: none; }
  .contacts li {
    display: flex; align-items: center; gap: 8px;
    font-size: 17px; color: var(--ink); height: 24px;
  }
  .contacts svg { width: 18px; height: 18px; fill: var(--teal); flex: none; }

  .dove-art {
    position: absolute; left: 278px; top: 150px;
    width: 136px; height: 160px;
    border-radius: 40% 60% 45% 55%;
    background: radial-gradient(circle at 45% 45%, var(--dove-tone), var(--dove-shade));
  }
</style>
</head>
<body>
<main class="canvas">
  <section class="card card--front">
    <div class="brand-name">Stillwater Care</div>
    <div class="person">
      <p class="person__name">Daniel Marsh</p>
      <p class="person__title">Managing Director</p>
      <div class="person__rule"></div>
    </div>
    <ul class="contacts">
      <li>
        <svg viewBox="0 0 24 24" aria-hidden="true"><path d="M6.6 10.8a15.1 15.1 0 0 0 6.6 6.6l2.2-2.2a1 1 0 0 1 1-.25 11.4 11.4 0 0 0 3.6.57 1 1 0 0 1 1 1V20a1 1 0 0 1-1 1A17 17 0 0 1 3 4a1 1 0 0 1 1-1h3.5a1 1 0 0 1 1 1c0 1.25.2 2.45.57 3.57a1 1 0 0 1-.25 1z"/></svg>
        555-0142-300
      </li>
      <li>
        <svg viewBox="0 0 24 24" aria-hidden="true"><path d="M2 5h20v14H2z M3.5 6.5 12 13l8.5-6.5" fill="none" stroke="var(--teal)" stroke-width="0"/><path d="M2 5h20v2l-10 7L2 7z"/><path d="M2 9l10 7 10-7v10H2z"/></svg>
        hello@stillwatercare.com
      </li>
      <li>
        <svg viewBox="0 0 24 24" aria-hidden="true"><circle cx="12" cy="12" r="10"/><path d="M2 12h20M12 2c3 3 3 17 0 20M12 2c-3 3-3 17 0 20M4 7h16M4 17h16" fill="none" stroke="#fff" stroke-width="1.4"/></svg>
        www.stillwatercare.com
      </li>
    </ul>
    <div class="dove-art" role="img" aria-label="Photograph of a white dove in flight"></div>
  </section>

  <section class="card card--back">
    <div class="brand-name">Stillwater Care</div>
  </section>
</main>
</body>
</html>
```